Group Medical Practice needs stationery, business cards etc. designed

We need stationery designed for a multisite practice that offers primary medical, dental and behavioral healthcare. We would like a design that is consistent for letterhead, business cards, Microsoft Outlook stationery etc. We have attached our new logo design.

Business

```html
<!DOCTYPE html>
<html lang="en">
<head>
<meta charset="utf-8">
<title>Cedar Ridge Health Services – Letterhead</title>
<link rel="stylesheet" href="https://fonts.googleapis.com/css2?family=Arimo:wght@400;700&display=swap">
<style>
  :root {
    --paper: #ffffff;
    --frame: #9a9a9a;
    --ink: #3a3a3a;
    --brand-green: #8cc63f;
  }
  * { margin: 0; padding: 0; box-sizing: border-box; }
  html, body { width: 849px; height: 1200px; overflow: hidden; background: var(--paper); }
  .letterhead {
    position: relative;
    width: 849px;
    height: 1200px;
    background: var(--paper);
    border: 2px solid var(--frame);
    font-family: "Arimo", Arial, sans-serif;
    color: var(--ink);
  }
  .brand {
    position: absolute;
    left: 50px;
    top: 72px;
    display: flex;
    align-items: center;
    gap: 12px;
  }
  .brand-dot {
    width: 20px; height: 20px;
    border-radius: 50%;
    background: var(--brand-green);
    flex: none;
  }
  .brand-name {
    color: var(--brand-green);
    font-weight: 700;
    font-size: 22px;
    line-height: 1.2;
    letter-spacing: 1px;
    text-transform: uppercase;
  }
  .contact {
    position: absolute;
    top: 67px;
    font-size: 14px;
    line-height: 16px;
  }
  .contact-phones { left: 420px; width: 196px; }
  .contact-place { left: 624px; width: 190px; }
  .contact-row { display: flex; align-items: center; gap: 11px; height: 20px; margin-bottom: 4px; white-space: nowrap; }
  .contact-row.address { height: 32px; margin-bottom: 14px; align-items: center; }
  .contact-icon { width: 17px; height: 17px; flex: none; fill: var(--brand-green); }
  .contact-icon.pin { height: 24px; }
</style>
</head>
<body>
<div class="letterhead">
  <div class="brand">
    <span class="brand-dot"></span>
    <div class="brand-name">Cedar Ridge<br>Health Services</div>
  </div>

  <div class="contact contact-phones">
    <div class="contact-row">
      <svg class="contact-icon" viewBox="0 0 18 18" aria-hidden="true"><path d="M2 6c0-2 3-3 7-3s7 1 7 3v1h-4V6H6v1H2z"/><path d="M4 8h10l1 7H3z"/><circle cx="9" cy="11.5" r="1.8" fill="#fff"/></svg>
      <span>020 7946 0321</span>
    </div>
    <div class="contact-row">
      <svg class="contact-icon" viewBox="0 0 18 18" aria-hidden="true"><rect x="5" y="1" width="8" height="16" rx="1.5"/><rect x="6.3" y="3" width="5.4" height="10" fill="#fff"/><circle cx="9" cy="15" r="0.9" fill="#fff"/></svg>
      <span>020 7946 0321</span>
    </div>
    <div class="contact-row">
      <svg class="contact-icon" viewBox="0 0 18 18" aria-hidden="true"><rect x="1" y="4" width="16" height="11" rx="1.5"/><path d="M2 5l7 5 7-5" fill="none" stroke="#fff" stroke-width="1.3"/></svg>
      <span>info@cedarridgehs.com</span>
    </div>
  </div>

  <div class="contact contact-place">
    <div class="contact-row address">
      <svg class="contact-icon pin" viewBox="0 0 18 18" aria-hidden="true"><path d="M9 1a6 6 0 0 0-6 6c0 4.5 6 10 6 10s6-5.5 6-10a6 6 0 0 0-6-6z"/><circle cx="9" cy="7" r="2.3" fill="#fff"/></svg>
      <span>Address will come here<br>Address will come here</span>
    </div>
    <div class="contact-row">
      <svg class="contact-icon" viewBox="0 0 18 18" aria-hidden="true"><circle cx="9" cy="9" r="8"/><g fill="none" stroke="#fff" stroke-width="1"><ellipse cx="9" cy="9" rx="3.2" ry="7"/><path d="M2 9h14M3 5.5h12M3 12.5h12"/></g></svg>
      <span>www.cedarridgehs.com</span>
    </div>
  </div>
</div>
</body>
</html>
```